Cobalt Ridge Lending Group, LLC
Project: Business Cards and Stationary
Business Cards and Stationary
Professional
Kevin T. Maldeno
President
4175 Harbor Glen Street Thousand Oaks, CA 91364
kmaldeno@Cobaltrdg.example
www.Cobaltrdg.example
NMLS #473058

```html
<!DOCTYPE html>
<html lang="en">
<head>
<meta charset="utf-8">
<title>Cobalt Ridge Lending Group, LLC — Business Cards</title>
<link href="https://fonts.googleapis.com/css2?family=Open+Sans:wght@400;600;700&display=swap" rel="stylesheet">
<style>
  :root {
    --backdrop: #262626;
    --card-white: #f7f7f7;
    --ink-blue: #0d4a98;
    --bright-blue: #1a7cc6;
    --ink-gray: #3a3a3a;
    --strip-gray: #444444;
    --rule: #1e4f8f;
  }
  * { margin: 0; padding: 0; box-sizing: border-box; }
  html, body { width: 1200px; height: 751px; overflow: hidden; }
  body {
    background: var(--backdrop);
    font-family: "Open Sans", Arial, sans-serif;
    position: relative;
  }
  .card {
    position: absolute;
    top: 218px;
    width: 492px;
    height: 282px;
    overflow: hidden;
  }
  .card--front { left: 91px; background: var(--card-white); }
  .card--back {
    left: 620px;
    background: radial-gradient(ellipse at 50% 40%, #2a8fd6 0%, #1668b4 45%, #0d4a98 100%);
  }
  .top-strip { position: absolute; left: 0; top: 0; width: 100%; height: 7px; background: var(--strip-gray); }
  .bottom-band {
    position: absolute; left: 0; bottom: 0; width: 100%; height: 9px;
    background: linear-gradient(90deg, var(--ink-blue) 0%, var(--bright-blue) 65%, var(--ink-blue) 100%);
  }
  .wordmark {
    position: absolute; left: 0; width: 100%; text-align: center;
    font-weight: 700; text-transform: uppercase; line-height: 1;
  }
  .card--front .wordmark { top: 42px; color: var(--ink-blue); }
  .card--back .wordmark { top: 100px; color: #ffffff; }
  .wordmark__main { display: block; font-size: 38px; letter-spacing: 1px; }
  .wordmark__sub { display: block; font-size: 13px; letter-spacing: 1.5px; margin-top: 7px; }
  .name-row {
    position: absolute; left: 22px; right: 20px; top: 152px;
    display: flex; align-items: center; gap: 6px;
  }
  .name-row__rule { flex: 1; height: 1px; background: var(--rule); }
  .name-row__name { font-size: 16px; font-weight: 700; color: var(--ink-blue); letter-spacing: 0.2px; }
  .name-row__title { font-size: 12.5px; color: var(--ink-gray); }
  .contact-list {
    position: absolute; left: 22px; top: 188px; list-style: none;
    font-size: 12px; color: var(--ink-gray);
  }
  .contact-list li { display: flex; align-items: center; height: 19.5px; }
  .contact-list svg { width: 14px; height: 14px; margin-right: 8px; fill: var(--ink-blue); }
  .office {
    position: absolute; right: 20px; top: 188px; text-align: right;
    font-size: 12px; color: var(--ink-gray); line-height: 19.5px;
  }
  .office__license { margin-bottom: 1px; }
  .office__web { color: var(--ink-blue); letter-spacing: 0.6px; }
</style>
</head>
<body>
  <section class="card card--front" aria-label="Business card front">
    <div class="top-strip"></div>
    <div class="wordmark">
      <span class="wordmark__main">Cobalt Ridge</span>
      <span class="wordmark__sub">Lending Group, LLC</span>
    </div>
    <div class="name-row">
      <span class="name-row__rule"></span>
      <span class="name-row__name">KEVIN T. MALDENO</span>
      <span class="name-row__title">- PRESIDENT</span>
      <span class="name-row__rule"></span>
    </div>
    <ul class="contact-list">
      <li><svg viewBox="0 0 16 16"><path d="M2 5c0-2 3-3 6-3s6 1 6 3v1h-3V5H5v1H2zM4 7h8l2 6H2z"/></svg>844.555.0172(TF)</li>
      <li><svg viewBox="0 0 16 16"><path d="M2 5c0-2 3-3 6-3s6 1 6 3v1h-3V5H5v1H2zM4 7h8l2 6H2z"/></svg>805.555.0148</li>
      <li><svg viewBox="0 0 16 16"><path d="M5 1h6a1 1 0 0 1 1 1v12a1 1 0 0 1-1 1H5a1 1 0 0 1-1-1V2a1 1 0 0 1 1-1zm1 2v9h4V3z"/></svg>818.555.0193</li>
      <li><svg viewBox="0 0 16 16"><path d="M1 4h14v1L8 9 1 5zm0 2.5 7 4 7-4V12H1z"/></svg>kmaldeno@Cobaltrdg.example</li>
    </ul>
    <div class="office">
      <p class="office__license">Lic No., NMLS #473058</p>
      <p>4175 Harbor Glen Street</p>
      <p>Thousand Oaks, CA 91364</p>
      <p class="office__web">www.Cobaltrdg.example</p>
    </div>
    <div class="bottom-band"></div>
  </section>

  <section class="card card--back" aria-label="Business card back">
    <div class="wordmark">
      <span class="wordmark__main">Cobalt Ridge</span>
      <span class="wordmark__sub">Lending Group, LLC</span>
    </div>
  </section>
</body>
</html>
```